An insurance broker wants to represent the company's vision visually and textually.

My company, with a total of 10 employees, developed a vision this year. Now, we want to display this vision in the form of a two-meter-high visual that will be mounted on the wall. This ensures that the vision is always visible to our employees, as well as to our clients and partners when they visit our office.

Here's my idea: the vision will be accompanied by a fitting image, with the text of the vision itself elegantly written in a beautiful font. Our vision reads: "Every company always has a perfectly tailored future solution for greater financial security, freedom, and joy."

A bit about my company: we are an insurance broker, and our services are primarily designed for corporate clients.

```html
<!DOCTYPE html>
<html lang="en">
<head>
<meta charset="UTF-8">
<title>Company Vision</title>
<link rel="stylesheet" href="https://fonts.googleapis.com/css2?family=Montserrat:wght@800;900&display=swap">
<style>
  :root {
    --brand-blue: #2f6fbd;
    --brand-blue-deep: #1f5aa6;
    --brand-blue-light: #4a86cf;
    --paper: #ffffff;
    --accent-yellow: #f7c51e;
    --text-light: #ffffff;
    --art-gold: #f2b632;
    --art-navy: #24497f;
  }
  * { margin: 0; padding: 0; box-sizing: border-box; }
  html, body {
    width: 804px;
    height: 1200px;
    overflow: hidden;
    background: var(--paper);
  }
  .vision-poster {
    position: relative;
    width: 804px;
    height: 1200px;
    overflow: hidden;
    background: var(--brand-blue);
    font-family: "Montserrat", Arial, sans-serif;
  }
  .backdrop {
    position: absolute;
    inset: 0;
    width: 804px;
    height: 1200px;
  }
  .vision-statement {
    position: absolute;
    left: 82px;
    top: 82px;
    width: 660px;
    text-transform: uppercase;
  }
  .vision-lead {
    color: var(--text-light);
    font-weight: 800;
    font-size: 43px;
    line-height: 1.08;
    letter-spacing: 0.5px;
  }
  .vision-highlight {
    margin-top: 6px;
    color: var(--accent-yellow);
    font-weight: 900;
    font-size: 57px;
    line-height: 1.04;
    letter-spacing: 0.3px;
  }
  .growth-illustration {
    position: absolute;
    left: 80px;
    top: 640px;
    width: 680px;
    height: 500px;
    border-radius: 6px;
    background:
      radial-gradient(ellipse at 62% 35%, rgba(247, 197, 30, 0.85) 0%, rgba(242, 182, 50, 0.35) 35%, rgba(242, 182, 50, 0) 60%),
      linear-gradient(160deg, var(--brand-blue-light) 0%, #8fb3dd 50%, #e6eef8 100%);
  }
</style>
</head>
<body>
  <main class="vision-poster">
    <svg class="backdrop" viewBox="0 0 804 1200" aria-hidden="true">
      <rect width="804" height="1200" fill="var(--brand-blue)"/>
      <polygon points="0,960 804,520 804,600 0,1040" fill="var(--brand-blue-deep)"/>
      <polygon points="0,1040 804,600 804,1200 0,1200" fill="var(--paper)"/>
    </svg>

    <section class="vision-statement">
      <h1 class="vision-lead">Every company always has a perfectly tailored future solution for</h1>
      <p class="vision-highlight">Greater financial security, freedom &amp; joy</p>
    </section>

    <div class="growth-illustration" role="img" aria-label="Isometric illustration of a rising yellow growth arrow over a chart monitor, with people, stacked gold coins, a calculator and a magnifying glass"></div>
  </main>
</body>
</html>
```